Technological Event Invitation

We need a invitation design for a technological event we are hosting along with our partner. The target of this event are Vice president, Managers and CEO of the most important companies (bank, insurrance companies, other) in the dominican republic.

It is a flat invitation and the size is 5” x 7”.

Title: API Management
"Transforma tu negocio con API Management a través de la estrategia de digitalización"
Date: Jueves 10 de Marzo del 2016
Time: 9:00 am - 5 pm.
Place: Resturant Casa Rivolta C/ Marcos Ibarra Lugo esq. Tomás Revel.
Host: Novaldo, SRL & KV Systems
RSVP: 809 555 47 13

The final design should have two logo one being Novaldo ( the company hosting the event) and KV logo ( partner). Please consider that the desgin should represent tecnhology world.

Target Market(s)

Financial Institutions,Corporations, Goverment Institution

Industry/Entity Type

Event

Requirements
Must have
• 1. Kv logo
• 2. novaldo Logo
• 3. The invitation should show that the is a tecnological event on APIM.
Nice to have
• our colors integrated on the invitations

```html
<!DOCTYPE html>
<html lang="es">
<head>
<meta charset="utf-8">
<title>API Management – Invitación</title>
<link rel="stylesheet" href="https://fonts.googleapis.com/css2?family=Exo+2:wght@400;500;600;700&display=swap">
<style>
  :root {
    --header-bg: #ffffff;
    --header-line: #d8d8d8;
    --brand-dark: #3a3d42;
    --brand-red: #e2231a;
    --partner-blue: #1d8fd6;
    --bg-deep: #1a0306;
    --bg-mid: #5a0a10;
    --bg-glow: #d41424;
    --text-light: #ffffff;
    --icon-red: #d9141f;
  }
  * { box-sizing: border-box; margin: 0; padding: 0; }
  html, body { width: 859px; height: 1200px; overflow: hidden; background: var(--bg-deep); }
  body { font-family: "Exo 2", sans-serif; color: var(--text-light); }

  .invitation { position: relative; width: 859px; height: 1200px; overflow: hidden; }

  .backdrop {
    position: absolute; inset: 0;
    background:
      radial-gradient(circle at 50% 36%, #ffe9ec 0, #ff5a6a 2%, var(--bg-glow) 9%, rgba(140,10,20,.85) 24%, var(--bg-mid) 40%, rgba(40,4,8,1) 70%, var(--bg-deep) 100%);
  }

  .header {
    position: absolute; top: 0; left: 0; width: 100%; height: 161px;
    background: var(--header-bg);
    border-bottom: 1px solid var(--header-line);
    display: flex; align-items: center; justify-content: space-between;
    padding: 0 56px 0 48px;
  }
  .host-brand { display: flex; align-items: center; gap: 14px; }
  .host-mark { width: 68px; height: 68px; border-radius: 50%; background: var(--brand-red); }
  .host-text { display: flex; flex-direction: column; }
  .host-name { font-size: 48px; font-weight: 700; color: var(--brand-dark); letter-spacing: 1px; text-transform: uppercase; line-height: 1; }
  .host-tagline { font-size: 19px; font-weight: 500; color: var(--brand-dark); letter-spacing: .5px; margin-top: 6px; }
  .partner-brand { font-size: 84px; font-weight: 700; color: var(--partner-blue); line-height: 1; }

  .title {
    position: absolute; top: 360px; left: 0; width: 100%;
    text-align: center; font-size: 78px; font-weight: 600; letter-spacing: 1px;
  }
  .tagline {
    position: absolute; top: 618px; left: 0; width: 100%;
    text-align: center; font-size: 40px; font-weight: 500; line-height: 54px;
  }

  .details {
    position: absolute; top: 868px; left: 0; width: 100%;
    list-style: none; display: flex; flex-direction: column; align-items: center; gap: 19px;
  }
  .details li { display: flex; align-items: center; gap: 10px; font-size: 26px; height: 32px; }
  .details strong { font-weight: 600; }
  .details svg { width: 32px; height: 32px; flex: none; }
</style>
</head>
<body>
<main class="invitation">
  <div class="backdrop" role="img" aria-label="Fondo tecnológico rojo oscuro con anillos concéntricos y un destello de luz central"></div>

  <header class="header">
    <div class="host-brand">
      <span class="host-mark"></span>
      <div class="host-text">
        <span class="host-name">Novaldo</span>
        <span class="host-tagline">IT CONSULTING AND SERVICES</span>
      </div>
    </div>
    <span class="partner-brand">KV</span>
  </header>

  <h1 class="title">API MANAGEMENT</h1>
  <p class="tagline">Transforma tu negocio con<br>API Management a través de la<br>estrategia de digitalización”</p>

  <ul class="details">
    <li>
      <svg viewBox="0 0 32 32"><circle cx="16" cy="16" r="16" fill="var(--icon-red)"/><rect x="9" y="10" width="14" height="13" rx="1.5" fill="none" stroke="#fff" stroke-width="2"/><line x1="9" y1="14" x2="23" y2="14" stroke="#fff" stroke-width="2"/><line x1="12" y1="8" x2="12" y2="11" stroke="#fff" stroke-width="2"/><line x1="20" y1="8" x2="20" y2="11" stroke="#fff" stroke-width="2"/></svg>
      <span><strong>Date:</strong> Jueves 10 de Marzo del 2016</span>
    </li>
    <li>
      <svg viewBox="0 0 32 32"><circle cx="16" cy="16" r="16" fill="var(--icon-red)"/><circle cx="16" cy="17" r="7" fill="none" stroke="#fff" stroke-width="2"/><polyline points="16,13 16,17 19,19" fill="none" stroke="#fff" stroke-width="2"/><line x1="9" y1="9" x2="11" y2="11" stroke="#fff" stroke-width="2"/><line x1="23" y1="9" x2="21" y2="11" stroke="#fff" stroke-width="2"/></svg>
      <span>Time: 9:00 am - 5 pm.</span>
    </li>
    <li>
      <svg viewBox="0 0 32 32"><circle cx="16" cy="16" r="16" fill="var(--icon-red)"/><path d="M16 7a6 6 0 0 1 6 6c0 5-6 12-6 12s-6-7-6-12a6 6 0 0 1 6-6z" fill="#fff"/><circle cx="16" cy="13" r="2.3" fill="var(--icon-red)"/></svg>
      <span><strong>Place:</strong> Resturant Casa Rivolta</span>
    </li>
    <li>
      <svg viewBox="0 0 32 32"><circle cx="16" cy="16" r="16" fill="var(--icon-red)"/><circle cx="16" cy="12" r="4" fill="#fff"/><path d="M9 24c0-5 3-7 7-7s7 2 7 7z" fill="#fff"/></svg>
      <span>C/ Marcos Ibarra Lugo esq. Tomás Revel.</span>
    </li>
    <li>
      <svg viewBox="0 0 32 32"><circle cx="16" cy="16" r="16" fill="var(--icon-red)"/><circle cx="16" cy="10" r="3" fill="#fff"/><rect x="9" y="15" width="14" height="3" fill="#fff"/><rect x="12" y="18" width="8" height="7" fill="#fff"/></svg>
      <span><strong>Host:</strong> Novaldo, SRL &amp; KV Systems</span>
    </li>
    <li>
      <svg viewBox="0 0 32 32"><circle cx="16" cy="16" r="16" fill="var(--icon-red)"/><rect x="11" y="7" width="10" height="18" rx="2" fill="#fff"/><rect x="13" y="10" width="6" height="6" fill="var(--icon-red)"/><circle cx="16" cy="21" r="1.3" fill="var(--icon-red)"/></svg>
      <span>RSVP: 809 555 47 13</span>
    </li>
  </ul>
</main>
</body>
</html>
```